Lumbrix Ventures Logo+Website+Social media design

We need a website/logo/social media design (LinkedIn, Facebook, Instagram, TikTok) for our 2 years-old company: Lumbrix Ventures. It's the company I've created to leave as a legacy for my sons, Lumbrix is the combination of Dalvo (my surname) and legacy.
We drive or support sales expansion. We also invest in promising companies and business operations with advisory and-or capital.
Our approach with our clients is tailor made, we leverage our expertise in Marketing, sales and our network to build a profitable sales expansion/presence.
The website needs to showcase the work we have done and it has to be easily updatable from a non-coder. The call to action is just one "contact us". I expect to connect a simple typeform after the CTA, and receive an email to our main email address.
I create a Team for every project/client. Lumbrix don't have employees, we gather the best people in my network to do the work. So our Team can go to 1 man band to 15+ people max.
In the Team I create I'll select Vibrant, very pro-active and energetic people, all with international experiences and track record.

I don't have a specific palette in mind, so feel free to create.

```html
<!DOCTYPE html>
<html lang="en">
<head>
<meta charset="utf-8">
<title>Lumbrix Ventures — Brand, Website and Social Set</title>
<link href="https://fonts.googleapis.com/css2?family=Poppins:wght@400;500;600;700;800&family=Kaushan+Script&family=Roboto+Slab:wght@500;700;900&display=swap" rel="stylesheet">
<style>
:root{
  --blue:#1a47ff;
  --navy:#14296b;
  --ink:#12172b;
  --muted:#8a90a2;
  --line:#e3e8f2;
  --board:#f3f7fb;
  --card:#ffffff;
  --grey-post:#e8e8e8;
  --photo-warm:#b7a79a;
  --photo-cool:#8d9bb0;
  --photo-skin:#c9a38a;
}
*{margin:0;padding:0;box-sizing:border-box}
html,body{width:720px;height:1200px;overflow:hidden;background:var(--board)}
body{font-family:'Poppins',sans-serif;color:var(--ink);position:relative}
.abs{position:absolute}
.photo{position:absolute;border-radius:2px}
.tiny{font-size:2.6px;line-height:3.6px;color:var(--muted)}
.eyebrow{font-size:2.6px;letter-spacing:.9px;color:var(--blue);text-transform:uppercase;font-weight:500}
.brand-name{font-weight:600;color:var(--ink);white-space:nowrap}
.brand-square{display:inline-block;background:var(--blue);vertical-align:middle}

/* website */
.site{left:90px;top:57px;width:213px;height:1085px;background:var(--card);overflow:hidden}
.hero{left:0;top:0;width:213px;height:142px;background:linear-gradient(180deg,#f7f9fd,#eef3fc);border-bottom:1px solid var(--blue)}
.nav-link{font-size:2.8px;color:var(--ink)}
.btn{background:var(--blue);color:#fff;border-radius:1px;font-size:2.6px;text-align:center;font-weight:500}
.stat{background:#fff;border-radius:2px;box-shadow:0 1px 4px rgba(20,41,107,.12);padding:3px}
.stat b{display:block;font-size:4.6px;color:var(--ink)}
.stat span{font-size:2.3px;color:var(--muted)}
.svc{background:#fff;border-radius:2px;box-shadow:0 1px 4px rgba(20,41,107,.08);padding:5px 4px}
.svc h4{font-size:4px;line-height:5.2px;font-weight:600;margin:4px 0 4px}
.svc a{font-size:2.4px;color:var(--blue);display:block;margin-top:2px}
.sec-title{font-size:4.6px;font-weight:600;text-align:center;width:213px;left:0}
.bar-label{font-size:2.6px;font-weight:600}
.bar{height:1px;background:var(--blue)}
.band-dark{left:0;top:389px;width:213px;height:123px;background:var(--navy)}
.feat{background:#fff;border-radius:2px;box-shadow:0 1px 4px rgba(20,41,107,.08)}
.feat h5{font-size:3.4px;font-weight:600;position:absolute;left:29px;top:8px}
.feat .tiny{position:absolute;left:29px;top:14px;width:48px;font-size:2.2px;line-height:3px}
.avatar{width:19px;height:19px;border-radius:50%;position:absolute;left:5px;top:8px;border:1px solid var(--blue)}
.faq-item{border-bottom:1px solid var(--line);font-size:2.8px;line-height:3.8px;color:#4a5064}
.band-blue{left:0;top:811px;width:213px;height:75px;background:var(--blue)}
.ring{width:14px;height:14px;border-radius:50%;box-shadow:0 1px 3px rgba(0,0,0,.2);border:1px solid #fff}
.footer{left:0;top:1036px;width:213px;height:49px;background:var(--navy)}
.foot-text{font-size:2.4px;line-height:3.4px;color:#fff}

/* posts */
.post{background:#fafbfd;overflow:hidden;box-shadow:0 2px 10px rgba(20,41,107,.06)}
.sq{width:8px;height:8px;border-radius:2px;position:absolute}
.dot-pill{width:8px;height:7px;border-radius:2px;background:#dfe6ff;position:absolute}
.script{font-family:'Kaushan Script',cursive;color:var(--navy)}
.headline{font-weight:700;color:var(--blue);letter-spacing:-.3px}
.post-foot{font-size:4px;line-height:4.6px}
.pill{background:var(--blue);color:#fff;border-radius:8px;text-align:center;font-weight:500}
.slab{font-family:'Roboto Slab',serif}
.grey{background:var(--grey-post)}
</style>
</head>
<body>

<!-- ============ WEBSITE ============ -->
<section class="abs site">
  <div class="abs hero">
    <svg class="abs" style="left:0;top:0" width="213" height="142" viewBox="0 0 213 142">
      <path d="M127 102 C135 80,140 95,147 84 C155 70,160 115,175 94 C182 84,190 90,198 76 C205 62,209 62,213 56" fill="none" stroke="#1a47ff" stroke-width=".6"/>
    </svg>
  </div>
  <div class="abs" style="left:22px;top:9px;font-size:3.2px"><span class="brand-square" style="width:5px;height:5px;margin-right:2px"></span><span class="brand-name">Lumbrix Ventures</span></div>
  <div class="abs nav-link" style="left:76px;top:10px">Home</div>
  <div class="abs nav-link" style="left:93px;top:10px">Pricing</div>
  <div class="abs nav-link" style="left:112px;top:10px">About</div>
  <div class="abs nav-link" style="left:129px;top:10px">Contact</div>
  <div class="abs nav-link" style="left:161px;top:10px;color:var(--blue)">Signup</div>
  <div class="abs btn" style="left:177px;top:7px;width:14px;height:8px;line-height:8px">Login</div>

  <h1 class="abs" style="left:22px;top:40px;font-size:8.8px;line-height:13px;font-weight:600;color:var(--navy)">Grow business<br>faster with value</h1>
  <p class="abs tiny" style="left:22px;top:69px;width:78px">We help growing teams open new markets, shape a sharper sales plan and find the right partners to scale with care.</p>
  <div class="abs btn" style="left:22px;top:93px;width:24px;height:8px;line-height:8px">Get a demo</div>
  <div class="abs" style="left:50px;top:94px;font-size:2.6px;color:var(--blue);line-height:6px">Contact Now</div>
  <div class="abs stat" style="left:121px;top:30px;width:45px;height:24px"><span>Sales</span><b>$35435</b><span>Compared to last year</span></div>
  <div class="abs stat" style="left:171px;top:56px;width:27px;height:27px;text-align:center">
    <svg width="9" height="9" viewBox="0 0 10 10"><circle cx="5" cy="5" r="4" fill="none" stroke="#1a47ff" stroke-width=".8"/><path d="M5 1V5H9" fill="none" stroke="#1a47ff" stroke-width=".8"/></svg>
    <b style="font-size:4.2px">80%</b><span>Sales Target</span></div>
  <div class="abs stat" style="left:106px;top:75px;width:24px;height:22px"><span>Orders</span><b>3,453</b><span style="color:#1ca14f">+1.5%</span></div>
  <div class="abs stat" style="left:147px;top:100px;width:44px;height:23px">
    <svg width="36" height="8" viewBox="0 0 36 8"><path d="M1 6 C6 1,9 7,14 4 S22 2,26 5 S32 1,35 3" fill="none" stroke="#1a47ff" stroke-width=".7"/></svg>
    <b>10,254</b><span>Visitors this year</span></div>

  <div class="abs eyebrow" style="left:0;top:165px;width:213px;text-align:center">Our Services</div>
  <h2 class="abs sec-title" style="top:171px">Boost your website traffic</h2>
  <p class="abs tiny" style="left:34px;top:182px;width:145px;text-align:center">Clear plans for every market you enter, built with a small team that cares about your numbers and your growth story.</p>

  <div class="abs svc" style="left:22px;top:208px;width:38px;height:75px">
    <svg width="8" height="8" viewBox="0 0 10 10"><circle cx="5" cy="5" r="4" fill="none" stroke="#1a47ff" stroke-width=".8"/><path d="M1 5H9M5 1C3 3,3 7,5 9M5 1C7 3,7 7,5 9" fill="none" stroke="#1a47ff" stroke-width=".6"/></svg>
    <h4>Speed Optimization</h4><p class="tiny">Quick pages keep every visitor close to the offer.</p><a>Learn More →</a></div>
  <div class="abs svc" style="left:66px;top:208px;width:38px;height:75px">
    <svg width="8" height="8" viewBox="0 0 10 10"><circle cx="5" cy="5" r="1.5" fill="none" stroke="#1a47ff" stroke-width=".7"/><path d="M1 1L4 4M9 1L6 4M1 9L4 6M9 9L6 6" stroke="#1a47ff" stroke-width=".7"/></svg>
    <h4>Marketing Analytics</h4><p class="tiny">Track each channel and keep the best ones growing.</p><a>Learn More →</a></div>
  <div class="abs svc" style="left:110px;top:208px;width:38px;height:75px">
    <svg width="8" height="8" viewBox="0 0 10 10"><path d="M2 8L8 2M5 2H8V5M2 6L4 8" fill="none" stroke="#1a47ff" stroke-width=".8"/></svg>
    <h4>Web Development</h4><p class="tiny">Sites your team can update without writing code.</p><a>Learn More →</a></div>
  <div class="abs svc" style="left:154px;top:208px;width:38px;height:75px">
    <svg width="8" height="8" viewBox="0 0 10 10"><rect x="1" y="2" width="8" height="5" fill="none" stroke="#1a47ff" stroke-width=".8"/><path d="M5 7V9M3 9H7" stroke="#1a47ff" stroke-width=".8"/></svg>
    <h4>Software Design</h4><p class="tiny">Simple tools shaped around the way you sell.</p><a>Learn More →</a></div>

  <div class="abs eyebrow" style="left:22px;top:300px">What we offer</div>
  <h3 class="abs" style="left:22px;top:306px;font-size:4.6px;line-height:6.2px;font-weight:600">Best Marketing Agency<br>For Your Business</h3>
  <p class="abs tiny" style="left:22px;top:323px;width:80px">Hand picked teams for each client, from one expert to a full crew of fifteen.</p>
  <div class="abs bar-label" style="left:22px;top:336px">Content &amp; Backlinks</div><div class="abs tiny" style="left:106px;top:336px">70%</div>
  <div class="abs bar" style="left:22px;top:341px;width:67px"></div><div class="abs" style="left:89px;top:341px;width:24px;height:1px;background:var(--line)"></div>
  <div class="abs bar-label" style="left:22px;top:349px">Web Development</div><div class="abs tiny" style="left:106px;top:349px">90%</div>
  <div class="abs bar" style="left:22px;top:354px;width:82px"></div>
  <div class="abs bar-label" style="left:22px;top:361px">Reporting &amp; Analysis</div><div class="abs tiny" style="left:106px;top:361px">80%</div>
  <div class="abs bar" style="left:22px;top:366px;width:75px"></div>
  <div class="abs" style="left:127px;top:309px;width:66px;height:45px;background:#2a2d35;border-radius:2px"></div>
  <div class="photo" role="img" aria-label="Laptop screen showing a consultant working at a desk" style="left:130px;top:312px;width:60px;height:39px;background:linear-gradient(135deg,#eef1f6,var(--photo-warm))"></div>
  <div class="abs" style="left:120px;top:354px;width:80px;height:3px;background:#c9ccd3;border-radius:0 0 3px 3px"></div>

  <div class="abs band-dark"></div>
  <div class="photo" role="img" aria-label="Photo of a young team reviewing work together at a table" style="left:23px;top:410px;width:72px;height:67px;background:linear-gradient(135deg,#d9dde3,var(--photo-cool))"></div>
  <div class="abs" style="left:47px;top:466px;width:54px;height:24px;background:var(--blue);color:#fff">
    <div class="abs" style="left:3px;top:8px;font-size:8px;font-weight:600;line-height:8px">+2500</div>
    <div class="abs" style="left:28px;top:4px;font-size:3.3px;line-height:4.4px;font-weight:500">Successful<br>Projects<br>Done</div>
  </div>
  <div class="abs eyebrow" style="left:110px;top:408px;color:#b9c4ea">What we do</div>
  <h3 class="abs" style="left:110px;top:414px;font-size:4.6px;line-height:7px;font-weight:500;color:#fff">Ensuring The Best Return On<br>Investment For SEO</h3>
  <p class="abs tiny" style="left:110px;top:435px;width:84px;color:#b9c4ea">Our teams shape the plan, open the doors and stay with you until the results are real.</p>
  <svg class="abs" style="left:110px;top:457px" width="7" height="7" viewBox="0 0 8 8"><circle cx="4" cy="4" r="4" fill="#1a47ff"/><path d="M2.3 4.1L3.5 5.2L5.8 2.9" fill="none" stroke="#fff" stroke-width=".8"/></svg>
  <div class="abs" style="left:123px;top:458px;font-size:3.4px;color:#fff;font-weight:500">Social Media Strategy</div>
  <p class="abs tiny" style="left:123px;top:464px;width:60px;color:#8f9bc8;font-size:2.2px;line-height:3px">Posts and plans that bring the right people to your door.</p>
  <svg class="abs" style="left:110px;top:479px" width="7" height="7" viewBox="0 0 8 8"><circle cx="4" cy="4" r="4" fill="#1a47ff"/><path d="M2.3 4.1L3.5 5.2L5.8 2.9" fill="none" stroke="#fff" stroke-width=".8"/></svg>
  <div class="abs" style="left:123px;top:480px;font-size:3.4px;color:#fff;font-weight:500">Search Engine Optimization</div>
  <p class="abs tiny" style="left:123px;top:486px;width:60px;color:#8f9bc8;font-size:2.2px;line-height:3px">Clear pages that climb and stay near the top of search.</p>

  <div class="abs eyebrow" style="left:0;top:536px;width:213px;text-align:center">Featured Services</div>
  <h2 class="abs sec-title" style="top:542px">The Best Solutions for Our Clients</h2>
  <p class="abs tiny" style="left:34px;top:553px;width:145px;text-align:center">From the first call to the final report, one team owns the result and keeps you informed at every step.</p>
  <div class="abs feat" style="left:22px;top:575px;width:81px;height:34px"><div class="photo avatar" role="img" aria-label="Photo of two colleagues reviewing data" style="background:var(--photo-warm)"></div><h5>Advanced Analytics</h5><p class="tiny">Numbers that show what works and what to fix.</p></div>
  <div class="abs feat" style="left:111px;top:575px;width:81px;height:34px"><div class="photo avatar" role="img" aria-label="Photo of a person at a computer" style="background:#5a6272"></div><h5>Digital Marketing</h5><p class="tiny">Campaigns tuned for each market you enter.</p></div>
  <div class="abs feat" style="left:22px;top:622px;width:81px;height:34px"><div class="photo avatar" role="img" aria-label="Photo of a team meeting" style="background:var(--photo-cool)"></div><h5>Business Innovation</h5><p class="tiny">Fresh ideas backed by advice and capital.</p></div>
  <div class="abs feat" style="left:111px;top:622px;width:81px;height:34px"><div class="photo avatar" role="img" aria-label="Photo of a laptop with charts" style="background:#b9c0cc"></div><h5>Reporting &amp; Analysis</h5><p class="tiny">Short, clear reports you can act on fast.</p></div>

  <div class="abs eyebrow" style="left:22px;top:692px">FAQ's</div>
  <h3 class="abs" style="left:22px;top:698px;font-size:4.6px;line-height:6.4px;font-weight:600">Find Out How It<br>Works And Ask Any<br>Questions.</h3>
  <div class="abs" style="left:22px;top:722px;width:76px;height:33px;background:var(--blue);padding:4px">
    <div style="font-size:3.3px;line-height:4.6px;color:#fff;font-weight:500">How do you build a team for my project?</div>
    <p class="tiny" style="color:#c9d3ff;margin-top:3px;font-size:2.2px;line-height:3px">We pick proven people from our network for each client and brief.</p></div>
  <div class="abs faq-item" style="left:22px;top:760px;width:76px;height:14px;padding:2px 4px">How fast can we<br>start working?<span style="position:absolute;right:2px;top:3px;color:var(--blue)">+</span></div>
  <div class="abs faq-item" style="left:22px;top:778px;width:76px;height:14px;padding:2px 4px">Do you invest in<br>new companies?<span style="position:absolute;right:2px;top:3px;color:var(--blue)">+</span></div>
  <div class="abs" style="left:126px;top:692px;width:66px;height:92px;background:#1d2230"></div>
  <div class="photo" role="img" aria-label="Photo of a smiling consultant in a chair" style="left:148px;top:725px;width:44px;height:59px;background:linear-gradient(160deg,#f2c230,#4a4f5e)"></div>
  <div class="abs" style="left:139px;top:698px;font-size:4.4px;line-height:6px;color:#fff;font-weight:500">Affordable<br>Prices</div>
  <div class="abs stat" style="left:117px;top:721px;width:33px;height:24px;padding:1px">
    <svg width="31" height="22" viewBox="0 0 31 22"><text x="1" y="4" font-size="2.4" font-family="Poppins" fill="#12172b">Growth</text><path d="M2 18 C7 12,10 16,14 11 S22 6,29 5" fill="none" stroke="#e0405a" stroke-width=".6"/><path d="M2 19 C8 16,12 18,17 14 S24 11,29 10" fill="none" stroke="#1a47ff" stroke-width=".6"/></svg></div>
  <div class="abs stat" style="left:109px;top:755px;width:44px;height:37px">
    <div style="height:3px;width:14px;background:var(--line);margin:3px 0"></div>
    <div style="display:flex;gap:3px"><div style="width:17px;height:9px;border:.6px solid var(--line);position:relative"><span style="position:absolute;left:7px;top:3px;width:3px;height:3px;border-radius:50%;background:#e0405a"></span></div><div style="width:17px;height:9px;background:var(--line)"></div></div>
    <div style="display:flex;gap:3px;margin-top:3px"><div style="width:17px;height:8px;background:var(--line)"></div><div style="width:17px;height:8px;border:.6px dashed #e0405a;position:relative"><span style="position:absolute;left:7px;top:2px;width:3px;height:3px;border-radius:50%;background:#e0405a"></span></div></div>
  </div>

  <div class="abs band-blue"></div>
  <div class="abs eyebrow" style="left:22px;top:823px;color:#c9d3ff">Why choose us</div>
  <h3 class="abs" style="left:22px;top:829px;font-size:4.6px;line-height:7px;font-weight:500;color:#fff">Your app is your tool for better<br>communication with your followers.</h3>
  <div class="photo" role="img" aria-label="Photo of a smiling team member in a denim jacket" style="left:23px;top:853px;width:52px;height:67px;background:linear-gradient(180deg,#4c3a30,#2a2320)"></div>
  <div class="abs" style="left:27px;top:898px;font-size:4.4px;line-height:6px;color:#fff;font-weight:500">Dedicated<br>Team</div>
  <div class="abs" style="left:27px;top:913px;font-size:2.4px;color:#fff">View More →</div>
  <div class="photo" role="img" aria-label="Photo of colleagues working together in a bright office" style="left:82px;top:853px;width:110px;height:67px;background:linear-gradient(160deg,#c8d3e0,#5f6f86)"></div>
  <div class="abs" style="left:86px;top:904px;font-size:4.4px;color:#fff;font-weight:500">Save Time &amp; Effort With Us</div>
  <div class="abs" style="left:86px;top:911px;font-size:2.4px;color:#fff">View More →</div>

  <div class="photo ring" role="img" aria-label="Client portrait" style="left:42px;top:941px;background:var(--photo-skin)"></div>
  <div class="photo ring" role="img" aria-label="Client portrait" style="left:154px;top:941px;background:#a07860"></div>
  <div class="photo ring" role="img" aria-label="Client portrait" style="left:23px;top:967px;background:#b58c74"></div>
  <div class="photo ring" role="img" aria-label="Client portrait" style="left:178px;top:967px;background:#9c7a66"></div>
  <div class="photo ring" role="img" aria-label="Client portrait" style="left:51px;top:992px;background:#6f5a4c"></div>
  <div class="photo ring" role="img" aria-label="Client portrait" style="left:143px;top:992px;background:#c4a08a"></div>
  <div class="abs eyebrow" style="left:0;top:961px;width:213px;text-align:center">Sales Marketing</div>
  <h3 class="abs" style="left:0;top:967px;width:213px;text-align:center;font-size:4.4px;line-height:7px;font-weight:600">Business Ethics You Can Trust. Create a<br>Unique Website for Your Business</h3>
  <div class="abs btn" style="left:95px;top:994px;width:24px;height:8px;line-height:8px">Get Started</div>

  <div class="abs footer"></div>
  <div class="abs" style="left:23px;top:1048px;width:26px;height:25px;background:var(--blue)"></div>
  <svg class="abs" style="left:75px;top:1050px" width="8" height="8" viewBox="0 0 10 10"><path d="M2 1L4 1L5 3.5L3.8 4.5C4.5 6,5.5 7,6.5 7.5L7.5 6.3L9.5 7.3L9.5 9C5 9,1 5,1 2Z" fill="none" stroke="#fff" stroke-width=".6"/></svg>
  <div class="abs foot-text" style="left:75px;top:1064px">+1(555)-010-7741<br>Call Us For Fast Support</div>
  <svg class="abs" style="left:123px;top:1051px" width="9" height="7" viewBox="0 0 10 8"><rect x=".5" y=".5" width="9" height="7" fill="none" stroke="#fff" stroke-width=".6"/><path d="M.5 .5L5 4.5L9.5 .5" fill="none" stroke="#fff" stroke-width=".6"/></svg>
  <div class="abs foot-text" style="left:122px;top:1064px">hello@lumbrixhq.com<br>Email Us for query</div>
  <svg class="abs" style="left:163px;top:1050px" width="7" height="9" viewBox="0 0 8 10"><path d="M4 9.5C1.5 6.5,.8 5,.8 3.5A3.2 3.2 0 0 1 7.2 3.5C7.2 5,6.5 6.5,4 9.5Z" fill="none" stroke="#fff" stroke-width=".6"/><circle cx="4" cy="3.5" r="1.1" fill="none" stroke="#fff" stroke-width=".6"/></svg>
  <div class="abs foot-text" style="left:161px;top:1064px">22 Harbor Lane<br>Portland, USA</div>
</section>

<!-- ============ BRAND NAME ============ -->
<div class="abs" style="left:362px;top:52px;height:56px;display:flex;align-items:center;gap:14px">
  <span class="brand-square" style="width:52px;height:52px;border-radius:3px"></span>
  <span class="brand-name" style="font-size:27px;letter-spacing:.2px">Lumbrix Ventures</span>
</div>

<!-- ============ POST 1 : wide ============ -->
<section class="abs post" style="left:395px;top:150px;width:288px;height:151px">
  <div class="abs" style="left:7px;top:10px;font-size:4.2px"><span class="brand-square" style="width:6px;height:6px;margin-right:2px"></span><span class="brand-name">Lumbrix Ventures</span></div>
  <div class="dot-pill" style="left:250px;top:6px"></div><div class="dot-pill" style="left:262px;top:6px"></div><div class="dot-pill" style="left:274px;top:6px"></div>
  <div class="sq" style="left:5px;top:59px;background:var(--blue)"></div>
  <div class="sq" style="left:5px;top:71px;background:var(--navy)"></div>
  <div class="sq" style="left:5px;top:83px;background:var(--blue)"></div>
  <div class="abs" style="left:29px;top:37px;font-size:8.6px;color:var(--navy)">We are</div>
  <div class="abs headline" style="left:29px;top:45px;font-size:17px;line-height:22px">SALES<br>MARKETING</div>
  <div class="abs script" style="left:29px;top:85px;font-size:21px;line-height:26px">Expert</div>
  <svg class="abs" style="left:141px;top:20px" width="140" height="94" viewBox="0 0 140 94"><path d="M2 20L9 18L11 84L4 72Z" fill="#1a47ff"/><path d="M104 8C118 6,128 10,130 22L138 82L127 76Z" fill="#1a47ff"/><path d="M10 78C16 92,40 94,70 90L20 90Z" fill="#1a47ff"/></svg>
  <div class="photo" role="img" aria-label="Overhead photo of a team around a meeting table with laptops and charts" style="left:149px;top:30px;width:127px;height:72px;border-radius:18px 6px 6px 24px;background:linear-gradient(135deg,#d8d2c6,#6d7480)"></div>
  <p class="abs tiny" style="left:30px;top:117px;width:246px;font-size:3.5px;line-height:4.6px">We build sales teams around your goals, open new markets with trusted partners and back promising firms with advice and capital so your growth lasts.</p>
  <svg class="abs" style="left:31px;top:136px" width="7" height="9" viewBox="0 0 8 10"><rect x=".5" y=".5" width="7" height="9" rx="1" fill="#1a47ff"/><path d="M2.3 2.3L3.3 2.3L3.8 3.6L3.2 4.1C3.5 4.9,4 5.4,4.6 5.7L5.1 5.1L6.1 5.6L6.1 6.6C4.2 6.6,2.3 4.6,2.3 2.3Z" fill="#fff"/></svg>
  <div class="abs post-foot" style="left:40px;top:136px"><span style="font-size:3.4px">More information call us</span><br><b style="color:var(--blue);font-weight:600">CALL# 000 111 - 222</b></div>
  <div class="abs pill" style="left:127px;top:135px;width:32px;height:13px;line-height:13px;font-size:6px">Contact</div>
  <div class="abs post-foot" style="left:200px;top:136px"><span style="font-size:3.4px;letter-spacing:.3px">www.lumbrixhq.com</span><br><b style="color:var(--blue);font-weight:600">VISIT OUR WEBSITE</b></div>
  <svg class="abs" style="left:266px;top:137px" width="9" height="9" viewBox="0 0 10 10"><circle cx="5" cy="5" r="4.4" fill="#1a47ff"/><path d="M.6 5H9.4M5 .6C3 3,3 7,5 9.4M5 .6C7 3,7 7,5 9.4" fill="none" stroke="#fff" stroke-width=".5"/></svg>
</section>

<!-- ============ POST 2 : square ============ -->
<section class="abs post" style="left:410px;top:359px;width:258px;height:259px">
  <div class="abs" style="left:6px;top:10px;font-size:4.2px"><span class="brand-square" style="width:6px;height:6px;margin-right:2px"></span><span class="brand-name">Lumbrix Ventures</span></div>
  <div class="dot-pill" style="left:217px;top:5px"></div><div class="dot-pill" style="left:229px;top:5px"></div><div class="dot-pill" style="left:241px;top:5px"></div>
  <svg class="abs" style="left:50px;top:20px" width="165" height="100" viewBox="0 0 165 100"><path d="M3 20L10 18L13 88L6 76Z" fill="#1a47ff"/><path d="M120 6C135 4,145 10,147 22L155 84L144 78Z" fill="#1a47ff"/><path d="M12 82C18 96,44 98,78 94L20 96Z" fill="#1a47ff"/></svg>
  <div class="photo" role="img" aria-label="Overhead photo of a team around a meeting table with laptops and charts" style="left:58px;top:33px;width:141px;height:80px;border-radius:20px 6px 6px 26px;background:linear-gradient(135deg,#d8d2c6,#6d7480)"></div>
  <div class="sq" style="left:6px;top:115px;background:var(--blue)"></div>
  <div class="sq" style="left:6px;top:127px;background:var(--navy)"></div>
  <div class="sq" style="left:6px;top:139px;background:var(--blue)"></div>
  <div class="sq" style="left:245px;top:115px;background:var(--blue)"></div>
  <div class="sq" style="left:245px;top:127px;background:var(--navy)"></div>
  <div class="sq" style="left:245px;top:139px;background:var(--blue)"></div>
  <div class="abs" style="left:0;top:126px;width:258px;text-align:center;font-size:11px;color:var(--navy)">We are</div>
  <div class="abs headline" style="left:0;top:138px;width:258px;text-align:center;font-size:23px;line-height:28px">SALES MARKETING</div>
  <div class="abs script" style="left:0;top:162px;width:258px;text-align:center;font-size:28px;line-height:34px">Expert</div>
  <p class="abs tiny" style="left:36px;top:208px;width:186px;text-align:center;font-size:3.5px;line-height:4.6px">We build sales teams around your goals, open new markets with trusted partners and back promising firms with advice and capital so growth lasts.</p>
  <svg class="abs" style="left:30px;top:241px" width="7" height="9" viewBox="0 0 8 10"><rect x=".5" y=".5" width="7" height="9" rx="1" fill="#1a47ff"/><path d="M2.3 2.3L3.3 2.3L3.8 3.6L3.2 4.1C3.5 4.9,4 5.4,4.6 5.7L5.1 5.1L6.1 5.6L6.1 6.6C4.2 6.6,2.3 4.6,2.3 2.3Z" fill="#fff"/></svg>
  <div class="abs post-foot" style="left:39px;top:241px"><span style="font-size:3.4px">More information call us</span><br><b style="color:var(--blue);font-weight:600">CALL# 000 111 - 222</b></div>
  <div class="abs pill" style="left:112px;top:241px;width:33px;height:13px;line-height:13px;font-size:6px">Contact</div>
  <div class="abs post-foot" style="left:164px;top:241px"><span style="font-size:3.4px;letter-spacing:.3px">www.lumbrixhq.com</span><br><b style="color:var(--blue);font-weight:600">VISIT OUR WEBSITE</b></div>
  <svg class="abs" style="left:229px;top:242px" width="9" height="9" viewBox="0 0 10 10"><circle cx="5" cy="5" r="4.4" fill="#1a47ff"/><path d="M.6 5H9.4M5 .6C3 3,3 7,5 9.4M5 .6C7 3,7 7,5 9.4" fill="none" stroke="#fff" stroke-width=".5"/></svg>
</section>

<!-- ============ POST 3 : wide grey ============ -->
<section class="abs post grey" style="left:395px;top:677px;width:288px;height:150px">
  <div class="abs slab" style="left:21px;top:6px;font-size:10px;font-weight:700;color:#3a3d45">GREAT IDEAS TO</div>
  <div class="abs slab" style="left:19px;top:8px;font-size:30px;line-height:36px;font-weight:900;color:var(--navy);letter-spacing:-1px">GROW</div>
  <div class="abs slab" style="left:108px;top:22px;width:34px;height:14px;background:var(--blue);color:#fff;font-size:9.5px;line-height:14px;text-align:center;font-weight:500">YOUR</div>
  <div class="abs slab" style="left:19px;top:37px;font-size:22px;line-height:26px;font-weight:900;color:#2b2e36">BUSINESS!</div>
  <div class="abs slab" style="left:20px;top:64px;width:120px;text-align:center;font-size:8px;line-height:10px;color:#3a3d45"><b>Grow</b> &amp; <b>Nuture</b> the<br><b>Ideas</b> You Have.</div>
  <svg class="abs" style="left:72px;top:88px" width="14" height="24" viewBox="0 0 14 24"><path d="M12 1L5 16M5 16L2 22L4 13M5 16L9 17L2 22" fill="none" stroke="#3a3d45" stroke-width=".8"/></svg>
  <div class="abs pill" style="left:55px;top:117px;width:44px;height:11px;line-height:11px;font-size:4.4px;font-weight:700">CONTACT US</div>
  <div class="abs" style="left:40px;top:130px;width:74px;text-align:center;font-size:7.8px;font-weight:700;color:#2b2e36">555-014-2290</div>
  <div class="abs" style="left:40px;top:140px;width:74px;text-align:center;font-size:4px;letter-spacing:.6px;color:#3a3d45">www.yourwebsite.com</div>
  <div class="photo" role="img" aria-label="Photo of a smiling businessman in glasses and tie holding a laptop" style="left:156px;top:14px;width:100px;height:133px;border-radius:40px 40px 0 0;background:linear-gradient(180deg,#d5d9df,#9fb6d6 55%,#7c95b8)"></div>
  <div class="abs" style="left:218px;top:10px;font-size:5.2px"><span class="brand-square" style="width:7px;height:7px;margin-right:2px"></span><span class="brand-name">Lumbrix Ventures</span></div>
  <svg class="abs" style="left:274px;top:50px" width="8" height="27" viewBox="0 0 8 27"><path d="M1 5L4 2L7 5M1 11L4 8L7 11M1 17L4 14L7 17M1 23L4 20L7 23" fill="none" stroke="#1a47ff" stroke-width="1.4"/></svg>
  <svg class="abs" style="left:252px;top:134px" width="27" height="8" viewBox="0 0 27 8"><path d="M1 1L4 4L1 7M6 1L9 4L6 7M11 1L14 4L11 7M16 1L19 4L16 7M21 1L24 4L21 7" fill="none" stroke="#2b2e36" stroke-width="1.3"/></svg>
  <div class="abs" style="left:0;top:147px;width:288px;height:3px;background:var(--blue)"></div>
</section>

<!-- ============ POST 4 : square grey ============ -->
<section class="abs post grey" style="left:410px;top:887px;width:258px;height:259px">
  <div class="abs" style="left:12px;top:13px;font-size:5.4px"><span class="brand-square" style="width:8px;height:8px;margin-right:3px"></span><span class="brand-name">Lumbrix Ventures</span></div>
  <svg class="abs" style="left:215px;top:11px" width="28" height="8" viewBox="0 0 28 8"><path d="M4 1L1 4L4 7M9 1L6 4L9 7M14 1L11 4L14 7M19 1L16 4L19 7M24 1L21 4L24 7" fill="none" stroke="#2b2e36" stroke-width="1.3"/></svg>
  <div class="abs slab" style="left:14px;top:51px;font-size:10.5px;font-weight:700;color:#3a3d45">GREAT IDEAS TO</div>
  <div class="abs slab" style="left:12px;top:54px;font-size:30px;line-height:36px;font-weight:900;color:var(--navy);letter-spacing:-1px">GROW</div>
  <div class="abs slab" style="left:103px;top:68px;width:31px;height:13px;background:var(--blue);color:#fff;font-size:9.5px;line-height:13px;text-align:center;font-weight:500">YOUR</div>
  <div class="abs slab" style="left:12px;top:83px;font-size:22px;line-height:26px;font-weight:900;color:#2b2e36">BUSINESS!</div>
  <div class="abs slab" style="left:0;top:138px;width:120px;text-align:center;font-size:8.4px;line-height:10.5px;color:#3a3d45"><b>Grow</b> &amp; <b>Nuture</b> the<br><b>Ideas</b> You Have.</div>
  <svg class="abs" style="left:53px;top:161px" width="14" height="25" viewBox="0 0 14 24"><path d="M12 1L5 16M5 16L2 22L4 13M5 16L9 17L2 22" fill="none" stroke="#3a3d45" stroke-width=".8"/></svg>
  <div class="abs pill" style="left:34px;top:207px;width:44px;height:11px;line-height:11px;font-size:4.4px;font-weight:700">CONTACT US</div>
  <div class="abs" style="left:19px;top:220px;width:74px;text-align:center;font-size:7.8px;font-weight:700;color:#2b2e36">555-014-2290</div>
  <div class="abs" style="left:19px;top:230px;width:74px;text-align:center;font-size:4px;letter-spacing:.6px;color:#3a3d45">www.yourwebsite.com</div>
  <div class="photo" role="img" aria-label="Photo of a smiling businessman in glasses and tie holding a laptop" style="left:140px;top:80px;width:118px;height:171px;border-radius:44px 44px 0 0;background:linear-gradient(180deg,#d5d9df,#9fb6d6 55%,#7c95b8)"></div>
  <svg class="abs" style="left:239px;top:93px" width="8" height="28" viewBox="0 0 8 27"><path d="M1 5L4 2L7 5M1 11L4 8L7 11M1 17L4 14L7 17M1 23L4 20L7 23" fill="none" stroke="#1a47ff" stroke-width="1.4"/></svg>
  <div class="abs" style="left:0;top:251px;width:258px;height:2px;background:var(--blue)"></div>
  <div class="abs" style="left:0;top:253px;width:258px;height:6px;background:#2b2e36"></div>
</section>

</body>
</html>
```